Etiketten für Charity Bier gesucht
Zielgruppe
Wir engagieren uns ehrenamtlich für Kinder in Afrika.
In Einsatz-Teams von freiwilligen Helfern, sammeln wir während 8 Monaten Spendengelder, um Kindern in Townships's Südafrikas eine Zukunft zu bauen, in dem wir nicht staatliche Kindertagesstätten engagierter einheimischer Frauen umbauen.
Vorher bestehen die KITA's nur aus rostigen Wellblechhütten, welche nicht isoliert sind und auf dem KITA Gelände befindet sich weder Rasen, noch ein Spielplatz.
Aufgabenstellung
Um Spenden zu sammeln, möchten wir ein Charity Bier auf den Markt bringen.
Infos zu den Maßen der Etiketten: Sie sollten nicht breiter als 8 cm sein. Wichtig ist, dass sich in der Ecke links oben keine Angaben befinden, da die obere linke Kante schräg nach oben verlaufen wird. Welche Angaben müssen zwingend auf den Etiketten zu finden sein?
Die Promill-Angaben (5.2% VOL)
Inhalts-Angabe (33cl) das Logo des Bierherstellers sollte auch mit auf die Etikette (nicht all zu gross) (siehe Bild Nr.2)
Die Info's zum Bier (Biersorte: Hochmoosbräu KLASSIK)
Der Name des Bier's sollte Charity Bier sein.
Wir möchten auf der Etikette auch folgendes unbedingt vermerken:
'Diese Flache (Bier) füllt 10 Breischalen für Kinder in Afrika'
Ansonsten haben wir überhaupt keine Vorstellung, was wir wörtlich noch auf die Etikette packen möchten (vielleicht fällt euch ja noch was tolles ein:-)
Was wir uns vom Design her so vorstellen:
Ich habe noch 3 Bilder (siehe Bild 3-4) dazugefügt, mit Designs, welche mir auf Anhieb sehr sehr gut gefallen (damit ihr einen Anhaltspunkt habt:-) Aber ich lasse mich auch gerne von anderen Design-Formen überraschen.

```html
<!DOCTYPE html>
<html lang="de">
<head>
<meta charset="utf-8">
<title>Charity Bier – Etikett</title>
<link rel="stylesheet" href="https://fonts.googleapis.com/css2?family=League+Gothic&family=Oswald:wght@500&family=Montserrat:wght@300&display=swap">
<style>
  :root {
    --label-turquoise: #6cd3d0;
    --label-white: #ffffff;
    --backdrop: #efefef;
  }
  html, body {
    margin: 0;
    padding: 0;
    width: 1200px;
    height: 960px;
    overflow: hidden;
    background: var(--backdrop);
  }
  .label {
    position: absolute;
    left: 320px;
    top: 40px;
    width: 560px;
    height: 880px;
    background: var(--label-turquoise);
    clip-path: polygon(0 122px, 100% 0, 100% 100%, 0 100%);
  }
  .label-art {
    display: block;
    width: 560px;
    height: 880px;
  }
  .brewery-name {
    font-family: "Oswald", sans-serif;
    font-weight: 500;
    font-size: 24px;
    fill: var(--label-white);
  }
  .beer-title {
    font-family: "League Gothic", sans-serif;
    font-weight: 400;
    fill: var(--label-white);
  }
  .beer-title--charity { font-size: 250px; }
  .beer-title--bier { font-size: 276px; }
  .label-white { fill: var(--label-white); }
  .label-turquoise { fill: var(--label-turquoise); }
  .donation-note {
    font-family: "Oswald", sans-serif;
    font-weight: 500;
    font-size: 21px;
    fill: var(--label-white);
  }
  .spec {
    font-family: "Montserrat", sans-serif;
    font-weight: 300;
    font-size: 23px;
    fill: var(--label-white);
  }
</style>
</head>
<body>
  <main class="label">
    <svg class="label-art" viewBox="0 0 560 880" role="group" aria-label="Charity Bier Etikett">
      <text class="brewery-name" x="542" y="92" text-anchor="end">Hochmoosbräu</text>

      <text class="beer-title beer-title--charity" x="8" y="385" textLength="542" lengthAdjust="spacingAndGlyphs">CHARITY</text>
      <text class="beer-title beer-title--bier" x="8" y="608" textLength="337" lengthAdjust="spacingAndGlyphs">BIER</text>

      <g class="star-badge">
        <circle class="label-white" cx="456" cy="506" r="63"/>
        <polygon class="label-turquoise"
          points="456,463 466,492 497,493 473,511 481,541 456,524 431,541 439,511 415,493 446,492"/>
      </g>

      <rect class="label-white divider" x="8" y="622" width="545" height="5"/>

      <g class="flag-icon">
        <polygon class="label-white" points="250,640 310,640 310,658 250,658 260,649"/>
        <polygon class="label-white" points="240,666 310,666 310,686 240,686 251,676"/>
      </g>

      <rect class="label-white info-rule" x="318" y="659" width="5" height="221"/>

      <g class="donation-note">
        <text x="340" y="672" textLength="213" lengthAdjust="spacingAndGlyphs">DER KAUF DIESER FLASCHE</text>
        <text x="340" y="705" textLength="206" lengthAdjust="spacingAndGlyphs">BIER FÜLLT 10 NAMI BREI-</text>
        <text x="340" y="738" textLength="199" lengthAdjust="spacingAndGlyphs">SCHALEN FÜR KINDER</text>
        <text x="340" y="771" textLength="157" lengthAdjust="spacingAndGlyphs">IN AFRIKA. DANKE!</text>
      </g>

      <text class="spec spec--alcohol" x="11" y="852">5,2 % VOL</text>
      <text class="spec spec--volume" x="229" y="852">33 cl</text>
    </svg>
  </main>
</body>
</html>
```